Noche de Salsa

We need a poster to promote a party. It is a salsa night at La Tortuga, a fun night out to dance, be with friends and have a few drinks. It is an informal occasion. The drinks will not be expensive and the snack will be typical mexican food.
La Tortuga is a campus for 8 local non-profit organizations but it also has high quality event venues and outdoor areas.
We would like a file for print (11x17") and a digital file for social media.
Enclosed:
- File with poster contents in spanish.
- La Tortuga logo
- Picture of palm trees at La Tortuga (you don't have to include this if another graphic fits best.
- Pic of the outside of the restaurant, where the dancing will take place. The restaurante is right in fron of the beach. THIS PICTURE DOES NOT NECESSARILY NEEDS TO BE PART OF THE POSTER.
- La Tortuga Fact Sheet for context.
Target Market(s)
Men and women from 25 to 50 years old.
American and mexican citizens.
Industry/Entity Type
Non-Profit
Colors
Designer to choose colors to be used in the design.
Look and feel
Each slider illustrates characteristics of the customer's brand and the style your logo design should communicate.

```html
<!DOCTYPE html>
<html lang="es">
<head>
<meta charset="utf-8">
<title>Noche de Salsa · La Tortuga</title>
<link rel="stylesheet" href="https://fonts.googleapis.com/css2?family=Questrial&family=Yellowtail&family=Caveat:wght@500&display=swap">
<style>
  :root {
    --page-bg: #e8e4dd;
    --paper: #ffffff;
    --ink: #111111;
    --text-grey: #444444;
    --accent-orange: #e2561f;
    --olive: #4b5a16;
    --art-red: #e32b20;
    --art-orange: #f07a1e;
    --art-yellow: #f7cf1a;
    --white: #ffffff;
  }
  * { margin: 0; padding: 0; box-sizing: border-box; }
  html, body {
    width: 890px; height: 1200px; overflow: hidden;
    background: var(--page-bg);
    font-family: "Questrial", "Century Gothic", sans-serif;
  }
  .poster {
    position: absolute; left: 75px; top: 30px;
    width: 740px; height: 1141px;
    background: var(--paper);
  }
  .hero-art {
    position: absolute; left: 97px; top: 74px;
    width: 564px; height: 521px;
  }
  .title { position: absolute; left: 0; top: 0; width: 100%; height: 100%; pointer-events: none; }
  .title-small {
    position: absolute; left: 385px; top: 600px;
    font-family: "Caveat", cursive; font-weight: 500;
    font-size: 38px; color: var(--ink); line-height: 1;
  }
  .title-main {
    position: absolute; left: 140px; top: 600px;
    font-family: "Yellowtail", cursive;
    font-size: 168px; color: var(--ink); line-height: 1;
  }
  .details { position: absolute; left: 0; width: 100%; text-align: center; }
  .details .label { color: var(--accent-orange); font-size: 14px; line-height: 1.3; }
  .details .value { color: var(--text-grey); font-size: 15px; line-height: 1.3; }
  .details-entry { top: 776px; }
  .details-date { top: 824px; }
  .brand {
    position: absolute; left: 0; top: 905px; width: 100%;
    display: flex; justify-content: center; align-items: center; gap: 14px;
  }
  .brand-dot { width: 26px; height: 26px; border-radius: 50%; background: var(--olive); }
  .brand-name { font-size: 50px; color: #333333; line-height: 1; }
  .address { position: absolute; left: 0; width: 100%; text-align: center; color: #333333; }
  .address-line { top: 1014px; font-size: 21px; }
  .address-note { top: 1040px; font-size: 9px; color: #777777; }
  .address-city { top: 1053px; font-size: 21px; }
  .contact-band {
    position: absolute; left: 0; bottom: 0; width: 100%; height: 58px;
    background: var(--olive); color: var(--white);
    display: flex; align-items: center; justify-content: center;
    font-size: 20px;
  }
</style>
</head>
<body>
  <main class="poster">
    <svg class="hero-art" role="img" aria-label="Illustration of a salsa dancing couple in silhouette over red, orange and yellow paint splashes" viewBox="0 0 564 521">
      <defs>
        <linearGradient id="art-tones" x1="0" y1="0" x2="1" y2="1">
          <stop offset="0" stop-color="var(--art-red)"/>
          <stop offset="0.5" stop-color="var(--art-orange)"/>
          <stop offset="1" stop-color="var(--art-yellow)"/>
        </linearGradient>
      </defs>
      <rect x="0" y="0" width="564" height="521" fill="url(#art-tones)"/>
    </svg>

    <div class="title-small">noche de</div>
    <h1 class="title-main">Salsa</h1>

    <div class="details details-entry">
      <p class="label">Entrada:</p>
      <p class="value">$100 pesos Incluye 1 bebida.</p>
    </div>
    <div class="details details-date">
      <p class="label">Viernes:</p>
      <p class="value">14 de noviembre 2014</p>
    </div>

    <div class="brand">
      <span class="brand-dot"></span>
      <span class="brand-name">La Tortuga</span>
    </div>

    <p class="address address-line">Acceso Playa #1480</p>
    <p class="address address-note">(al final de la calle Palmar, junto al antiguo muelle)</p>
    <p class="address address-city">Col. Las Palmas, C.P. 23090, La Paz, B.C.S.</p>

    <footer class="contact-band">Más informes al 140-3317 | info@latortuga.org</footer>
  </main>
</body>
</html>
```